Moss&Lark

I'm writing a book and need a front and back cover for the book.

IMPORTANT DETAILS:
TITLE: Moss & Lark
SUBTITLE: Twelve empowering true stories of women who found strength and hope in times of darkness and despair.
AUTHORS: Marnie Tolliver & Dalia Pratt
1. The book is about WOMEN'S stories of struggle (MOSS) and overcoming them with a hopeful and inspiring story at the end (LARK). So the cover of the book should depict these opposing / conflicting ideas.

2. The cover needs to be clean and simple

3. a.The font for the word MOSS should look stronger/bolder/more intense/sturdier/a little more masculine....
b. The ampersand (&) between Moss & Lark should tie the two fonts together
c. The font for the word LARK should look fluid/clean/EASY-TO-READ cursive script

4. I'm open to different color fonts with a limit of 3 colors MAX

5. For the back cover: This will be a collection of stories from 12 total authors so the back cover needs to have room for 12 faces somehow.

Looking forward to it.

```html
<!DOCTYPE html>
<html lang="en">
<head>
<meta charset="UTF-8">
<title>Moss &amp; Lark — Book Cover</title>
<link rel="stylesheet" href="https://fonts.googleapis.com/css2?family=Oswald:wght@300;400&family=Cormorant+Garamond:ital,wght@1,500&display=swap">
<style>
  :root {
    --backdrop: #ddca8e;
    --ink-white: #ffffff;
    --night: #050505;
    --sky-top: #3c7bb0;
    --sky-mid: #7fb3c4;
    --sun-glow: #f6c235;
    --sun-deep: #e79a1e;
    --ground: #0b0906;
  }
  html, body {
    margin: 0;
    padding: 0;
    width: 1200px;
    height: 799px;
    overflow: hidden;
    background: var(--backdrop);
  }
  .canvas {
    position: relative;
    width: 1200px;
    height: 799px;
  }
  .book-cover {
    position: absolute;
    left: 408px;
    top: 93px;
    width: 397px;
    height: 605px;
    background: var(--night);
    overflow: hidden;
  }
  .cover-scene {
    position: absolute;
    left: 0;
    top: 0;
    width: 100%;
    height: 356px;
    background: linear-gradient(
      to bottom,
      var(--sky-top) 0%,
      var(--sky-mid) 40%,
      var(--sun-glow) 66%,
      var(--sun-deep) 82%,
      var(--ground) 96%,
      var(--night) 100%
    );
  }
  .title {
    position: absolute;
    left: 0;
    top: 0;
    width: 100%;
    height: 200px;
    margin: 0;
    font-weight: normal;
    color: var(--ink-white);
  }
  .title-strong {
    position: absolute;
    left: 40px;
    top: 38px;
    font-family: "Oswald", sans-serif;
    font-weight: 400;
    font-size: 68px;
    line-height: 1;
    white-space: nowrap;
  }
  .title-amp {
    position: absolute;
    left: 192px;
    top: 50px;
    font-family: "Cormorant Garamond", serif;
    font-style: italic;
    font-weight: 500;
    font-size: 80px;
    line-height: 1;
  }
  .title-script {
    position: absolute;
    left: 176px;
    top: 114px;
    font-family: "Cormorant Garamond", serif;
    font-style: italic;
    font-weight: 500;
    font-size: 66px;
    line-height: 1;
    letter-spacing: 1px;
    white-space: nowrap;
  }
  .subtitle {
    position: absolute;
    left: 0;
    top: 382px;
    width: 100%;
    margin: 0;
    text-align: center;
    font-family: "Oswald", sans-serif;
    font-weight: 300;
    font-size: 24px;
    line-height: 40px;
    color: var(--ink-white);
  }
  .authors {
    position: absolute;
    left: 0;
    top: 558px;
    width: 100%;
    margin: 0;
    text-align: center;
    font-family: "Oswald", sans-serif;
    font-weight: 300;
    font-size: 17px;
    color: var(--ink-white);
  }
</style>
</head>
<body>
<div class="canvas">
  <div class="book-cover">
    <div class="cover-scene" role="img" aria-label="Sunset sky over a dark horizon with the silhouette of a woman sitting on a bench"></div>
    <h1 class="title">
      <span class="title-strong">MOSS</span>
      <span class="title-amp">&amp;</span>
      <span class="title-script">LARK</span>
    </h1>
    <p class="subtitle">Twelve empowering true stories of<br>women who found strength and hope<br>in times of darkness and despair.</p>
    <p class="authors">Marnie Tolliver &amp; Dalia Pratt</p>
  </div>
</div>
</body>
</html>
```